Bright Harbor Recordings looking for artwork for the next release EP

We are an electronic record label looking for a piece of artwork designed for the next EP release. It needs to follow the same style as previous releases. We need the finished design as saved layers (background. foreground, details) as we use this for creating teaser trailer videos. This is for a digital-only release, it won't actually be printed out for CDs.
Dimensions 3000 x 3000

Target Market(s)

Electronic

Colors

Designer to choose colors to be used in the design.

Requirements
Must have
• See attachments for the style of artwork we are looking for. Needs to be in the same format with the same grainy look. Finished design must be delieved as saved layers (background. foreground, details)
Nice to have
• The artist's name is Velvet Lantern , and the name of the EP is called 'Glass Orbit'

```html
<!DOCTYPE html>
<html lang="en">
<head>
<meta charset="utf-8">
<title>Glass Orbit — Velvet Lantern</title>
<link rel="stylesheet" href="https://fonts.googleapis.com/css2?family=Saira+Condensed:ital,wght@0,300;1,300&display=swap">
<style>
  :root {
    --night: #1c1640;
    --dusk: #3a1f4a;
    --ember: #f0203a;
    --coral: #f7606a;
    --haze: #e8c9c2;
    --magenta: #d41a6a;
    --rose: #f38c8a;
    --ridge: #4a2040;
    --ink: #ffffff;
  }
  html, body {
    margin: 0;
    padding: 0;
    width: 1200px;
    height: 1200px;
    overflow: hidden;
    background: var(--night);
  }
  .cover {
    position: relative;
    width: 1200px;
    height: 1200px;
    overflow: hidden;
  }
  .artwork {
    position: absolute;
    inset: 0;
    background:
      linear-gradient(180deg, transparent 0%, transparent 60%, rgba(212,26,106,0.85) 66%, rgba(243,140,138,0.9) 82%, rgba(74,32,64,0.95) 92%, #4a3050 100%),
      radial-gradient(circle at 68% 54%, var(--ember) 0%, var(--coral) 22%, rgba(247,96,106,0.55) 34%, transparent 48%),
      radial-gradient(circle at 100% 0%, var(--haze) 0%, rgba(232,201,194,0.4) 22%, transparent 42%),
      linear-gradient(90deg, var(--night) 0%, var(--dusk) 40%, #6a2a48 60%, #c85868 100%);
  }
  .grain {
    position: absolute;
    inset: 0;
    width: 1200px;
    height: 1200px;
    mix-blend-mode: overlay;
    opacity: 0.45;
    pointer-events: none;
  }
  .credits {
    position: absolute;
    left: 68px;
    top: 62px;
    color: var(--ink);
    font-family: "Saira Condensed", "Arial Narrow", sans-serif;
    font-weight: 300;
  }
  .credits__title {
    margin: 0;
    font-size: 38px;
    line-height: 1.1;
    font-weight: 300;
    padding-bottom: 4px;
    border-bottom: 1.5px solid var(--ink);
    width: 185px;
    white-space: nowrap;
  }
  .credits__artist {
    margin: 6px 0 0 2px;
    font-size: 38px;
    line-height: 1.1;
    font-style: italic;
    font-weight: 300;
    white-space: nowrap;
  }
</style>
</head>
<body>
  <main class="cover">
    <div class="artwork" role="img" aria-label="Illustration: a pale setting sun behind layered magenta mountain ridges under a glowing red haze and dark night sky"></div>
    <svg class="grain" viewBox="0 0 1200 1200" aria-hidden="true">
      <filter id="film-grain">
        <feTurbulence type="fractalNoise" baseFrequency="0.9" numOctaves="2" stitchTiles="stitch"/>
        <feColorMatrix type="saturate" values="0"/>
      </filter>
      <rect width="1200" height="1200" filter="url(#film-grain)"/>
    </svg>
    <header class="credits">
      <h1 class="credits__title">Glass Orbit</h1>
      <p class="credits__artist">Velvet Lantern</p>
    </header>
  </main>
</body>
</html>
```